Non-Profit Needs Web Redesign for Revolutionary Grieving Process

We need a redesign of our website that represents the expansive social goal of changing the worldview of how our culture understands and can heal from the universal experience of grief. The Bright Harbor process is a revolutionary method that allows an individual to resolve the underlying issue that cause the painful experience of loss.The color scheme should be in the green family that is soft and light yet professional and connotes change and growth. The final design should communicate simplistically with white space and strong typography a global viewpoint of change in a fundamental human experience. The redesign should represent the non-profit organization's perspective of openness and possibility without being flashy or corporate. see www.lumevaro.org
Target Market(s)
Grief professional, hospitals, hospices
Industry/Entity Type
Non Profit
Coding
Coded - Design and coding required
Number of Pages Required
1 page
Look and feel

```html
<!DOCTYPE html>
<html lang="en">
<head>
<meta charset="utf-8">
<title>Lumevaro.org – A Revolutionary Grieving Process</title>
<link rel="stylesheet" href="https://fonts.googleapis.com/css2?family=Open+Sans:wght@300;400;600;700;800&display=swap">
<style>
:root{
  --green:#8cc63f;
  --green-dark:#5e9a1e;
  --heading-green:#6aaa1e;
  --teal:#1fb99a;
  --ink:#222;
  --grey-text:#6b6b6b;
  --band:#e4e4e4;
  --footer:#0d0d0d;
  --white:#fff;
}
*{box-sizing:border-box;margin:0;padding:0}
html,body{width:1200px;height:2164px;overflow:hidden;background:var(--white);font-family:"Open Sans",Arial,sans-serif;color:var(--ink)}
.page{position:relative;width:1200px;height:2164px}
.abs{position:absolute}

/* header */
.brand{left:168px;top:22px}
.brand-name{font-size:50px;font-weight:800;color:var(--ink);letter-spacing:-1px;line-height:1}
.brand-tag{font-size:17px;font-weight:600;color:var(--ink);margin-top:4px}
.search{left:830px;top:70px;width:220px;height:36px;border:1px solid #ccc;border-radius:4px;background:#f4f4f4;font-size:15px;color:#999;padding:7px 12px}

.nav{left:150px;top:150px;width:900px;height:44px;background:var(--green);display:flex;align-items:center;padding-left:10px}
.nav a{color:var(--white);text-decoration:none;font-size:16px;font-weight:600;padding:0 10px;height:44px;line-height:44px}
.nav a.active{background:var(--green-dark)}

/* hero */
.hero-photo{left:0;top:198px;width:1200px;height:522px;background:linear-gradient(100deg,#b9b6ad 0%,#9e9a91 40%,#7f7b73 70%,#a8a49b 100%)}
.hero-text{left:168px;top:250px;width:520px;color:var(--white)}
.hero-text h1{font-weight:300;font-size:100px;line-height:1;letter-spacing:-2px}
.hero-text h1 strong{display:block;font-weight:700;color:var(--green);font-size:78px;letter-spacing:-1px;margin-top:4px}
.hero-quote{font-size:25px;line-height:1.3;margin-top:24px;width:440px;font-family:Georgia,serif}
.hero-sub{font-size:17px;line-height:1.35;width:470px;margin-top:10px}
.btn{display:inline-block;margin-top:22px;background:var(--teal);color:var(--white);font-weight:700;font-size:20px;padding:12px 28px;border-radius:3px;text-decoration:none;letter-spacing:.5px}

/* sections */
.sec h2{font-size:34px;font-weight:700;color:var(--heading-green);line-height:1.2;margin-bottom:10px}
.sec p{font-size:18px;line-height:1.4;color:var(--grey-text)}
.more{display:block;font-size:17px;font-weight:700;color:var(--ink);text-decoration:none;margin-top:6px}
.photo{background:linear-gradient(160deg,#e9e7e3,#cfcbc4)}
.sec-1{left:168px;top:775px;width:530px}
.sec-1 .more{text-align:right}
.photo-1{left:720px;top:735px;width:210px;height:295px}
.photo-2{left:170px;top:1055px;width:310px;height:285px}
.sec-2{left:510px;top:1065px;width:500px;text-align:right}
.sec-3{left:168px;top:1390px;width:600px}
.sec-3 .more{text-align:right}
.photo-3{left:800px;top:1345px;width:210px;height:295px}

/* testimonials */
.band{left:0;top:1652px;width:1200px;height:410px;background:var(--band)}
.quote-badge{left:568px;top:1620px;width:64px;height:64px;border-radius:50%;background:var(--band);display:flex;align-items:center;justify-content:center}
.card{top:1720px;width:395px;height:170px;background:var(--teal);color:var(--white);padding:18px 24px;font-size:18px;line-height:1.3;text-align:justify}
.card-1{left:180px}
.card-2{left:625px}
.author{top:1900px;font-size:17px;color:#333}
.author-1{left:480px}
.author-2{left:935px}
.avatar{top:1905px;width:72px;height:72px;border-radius:50%;background:linear-gradient(#c9b9a6,#8c7b6a)}
.avatar-1{left:210px}
.avatar-2{left:655px}
.arrow{top:1795px}
.arrow-l{left:140px}
.arrow-r{left:1032px}

/* footer */
.footer{left:0;top:2062px;width:1200px;height:102px;background:var(--footer)}
.foot-links{left:0;top:2074px;width:1200px;text-align:center;font-size:16px;color:var(--white)}
.foot-links a{color:var(--white);text-decoration:none;margin:0 8px}
.copy{left:168px;top:2132px;font-size:14px;color:#ddd}
</style>
</head>
<body>
<div class="page">

  <header>
    <div class="abs brand">
      <div class="brand-name">Lumevaro.org</div>
      <div class="brand-tag">A Revolutionary Grieving Process</div>
    </div>
    <div class="abs search">search here...</div>
    <nav class="abs nav">
      <a class="active" href="#">Home</a>
      <a href="#">The Process</a>
      <a href="#">Testimonials</a>
      <a href="#">Get Support</a>
      <a href="#">Professional Training</a>
      <a href="#">Blog</a>
      <a href="#">Contact Us</a>
      <a href="#">About</a>
    </nav>
  </header>

  <section>
    <div class="abs hero-photo" role="img" aria-label="Photo of a couple sitting together on a beach, looking out to sea"></div>
    <div class="abs hero-text">
      <h1>Become<strong>Lumevaro</strong></h1>
      <p class="hero-quote">“Welcome to a radical new way to grieve that actually works...”.</p>
      <p class="hero-sub">Transform the pain of grief into a revitalized experience of love and acceptance.</p>
      <a class="btn" href="#">LEARN TODAY</a>
    </div>
  </section>

  <section class="abs sec sec-1">
    <h2>What is Bright Harbor?</h2>
    <p>Bright Harbor is the process of letting go of an attachment. An attachment is defined as anything external that gives identity and meaning to one's life that when lost or taken away causes a deep feeling of loss and emptiness. Attachments are as intertwined in one's life as to be unrecognizable...</p>
    <a class="more" href="#">Read More &gt;</a>
  </section>
  <div class="abs photo photo-1" role="img" aria-label="Photo of a man sitting alone on a wooden park bench"></div>

  <div class="abs photo photo-2" role="img" aria-label="Photo of two women sitting on the grass in conversation"></div>
  <section class="abs sec sec-2">
    <h2>The Bright Harbor Process</h2>
    <p>Bright Harbor should take no more than three months but can be accomplished very quickly if done deeply and with focused intent. After purging the ache of the loss through Bright Harbor, an individual will experience a revitalized sense of love and appreciation in its place.</p>
    <a class="more" href="#">Read More &gt;</a>
  </section>

  <section class="abs sec sec-3">
    <h2>Understanding Bright Harbor</h2>
    <p>Grieving may be one of the most misunderstood experiences of human nature. In the Bright Harbor process, grieving is not the experience of the emotional pain of the loss of the person or object, it is the experience of the pain of the loss of what the person or object represented...</p>
    <a class="more" href="#">Read More &gt;</a>
  </section>
  <div class="abs photo photo-3" role="img" aria-label="Photo of a father walking hand in hand with a small child"></div>

  <section>
    <div class="abs band"></div>
    <div class="abs quote-badge">
      <svg width="30" height="24" viewBox="0 0 30 24"><path d="M2 22V12C2 6 5 2 11 1v4C8 6 7 8 7 11h5v11zM17 22V12c0-6 3-10 9-11v4c-3 1-4 3-4 6h5v11z" fill="var(--teal)"/></svg>
    </div>
    <svg class="abs arrow arrow-l" width="28" height="40" viewBox="0 0 28 40"><path d="M22 4 6 20l16 16" fill="none" stroke="var(--teal)" stroke-width="5"/></svg>
    <svg class="abs arrow arrow-r" width="28" height="40" viewBox="0 0 28 40"><path d="M6 4l16 16L6 36" fill="none" stroke="var(--teal)" stroke-width="5"/></svg>
    <blockquote class="abs card card-1">Lorem ipsum dolor sit amet, consectetur adipiscing elit. Morbi sed vehicula nunc. Ut sed efficitur nulla, ac dictum velit. Nulla sagittis nisi vel sapien finibus, ac aliquet libero tempor. Phasellus gravida...</blockquote>
    <blockquote class="abs card card-2">Lorem ipsum dolor sit amet, consectetur adipiscing elit. Morbi sed vehicula nunc. Ut sed efficitur nulla, ac dictum velit. Nulla sagittis nisi vel sapien finibus, ac aliquet libero tempor. Phasellus gravida...</blockquote>
    <div class="abs avatar avatar-1" role="img" aria-label="Portrait photo of the reviewer"></div>
    <div class="abs avatar avatar-2" role="img" aria-label="Portrait photo of the reviewer"></div>
    <div class="abs author author-1">- Marisa T.</div>
    <div class="abs author author-2">- Owen K.</div>
  </section>

  <footer>
    <div class="abs footer"></div>
    <div class="abs foot-links"><a href="#">Contact</a>| <a href="#">About</a>| <a href="#">Blog</a>| <a href="#">Support</a></div>
    <div class="abs copy">Copyright 2013 Lumevaro.org see Terms of Use herein</div>
  </footer>

</div>
</body>
</html>
```